Velmoria - 3D medical animations and high end visual content

Our company creates high end visual content and animations for medical global companies.
Our website - www.velmoria-studio.example
We would like to have an amazing business card for our CEO that he can use in the following exhebitions he is going to attend.
It is very important that the design will be memorable and diffrent. It has to reflect our brand design (you can have it from our website)
We would like to transmit innovation, prestige, luxury, aesthetics.
The card has to be Double Sided

Target Market(s)

Marketing managers in medical global companys

Industry/Entity Type

It Company

Contact Information for Business Card

Requirements
Nice to have
• It is very important that the design will be memorable and diffrent. It has to reflect our brand design (you can have it from our website)

```html
<!DOCTYPE html>
<html lang="en">
<head>
<meta charset="utf-8">
<title>Velmoria – Business Card</title>
<link href="https://fonts.googleapis.com/css2?family=Jost:wght@400;500;600&display=swap" rel="stylesheet">
<style>
  :root {
    --page: #ffffff;
    --card: #0a0d0e;
    --teal: #2fb8b6;
    --white: #ffffff;
    --soft: #d9dcdd;
  }
  * { margin: 0; padding: 0; box-sizing: border-box; }
  html, body {
    width: 1200px; height: 720px; overflow: hidden;
    background: var(--page);
    font-family: "Jost", "Century Gothic", sans-serif;
  }
  .card {
    position: absolute; left: 46px; top: 40px;
    width: 1105px; height: 631px;
    background: var(--card);
    overflow: hidden;
  }
  .brand {
    position: absolute; left: 103px; top: 255px; width: 396px;
    text-align: center;
    color: var(--white);
    font-size: 56px; font-weight: 500; letter-spacing: 2px;
    line-height: 1;
  }
  .divider {
    position: absolute; left: 544px; top: 86px;
    width: 3px; height: 458px;
    background: linear-gradient(to bottom, transparent, #cfd3d4 30%, #ffffff 50%, #cfd3d4 70%, transparent);
  }
  .person { position: absolute; left: 592px; top: 175px; color: var(--white); }
  .person-name { font-size: 40px; font-weight: 600; line-height: 1; }
  .person-role { margin-top: 20px; font-size: 21px; font-weight: 400; color: var(--soft); }
  .contacts { position: absolute; left: 596px; top: 295px; list-style: none; }
  .contact {
    display: flex; align-items: center; gap: 16px;
    height: 46px;
    color: var(--white); font-size: 28px; font-weight: 400;
  }
  .contact svg { width: 22px; height: 24px; flex: none; fill: var(--teal); }
  .footer-shape { position: absolute; left: 0; top: 0; }
  .website {
    position: absolute; left: 651px; top: 582px;
    color: var(--white); font-size: 28px; font-weight: 400;
    line-height: 1;
  }
</style>
</head>
<body>
  <div class="card">
    <div class="brand">VELMORIA</div>
    <div class="divider"></div>

    <div class="person">
      <div class="person-name">Noam Adler</div>
      <div class="person-role">Founder &amp; CEO</div>
    </div>

    <ul class="contacts">
      <li class="contact">
        <svg viewBox="0 0 22 24" aria-hidden="true"><path d="M6 1h10a2 2 0 0 1 2 2v18a2 2 0 0 1-2 2H6a2 2 0 0 1-2-2V3a2 2 0 0 1 2-2zm0 3v14h10V4zm5 15.5a1 1 0 1 0 0 2 1 1 0 0 0 0-2z"/></svg>
        <span>+972-50-1234567</span>
      </li>
      <li class="contact">
        <svg viewBox="0 0 22 24" aria-hidden="true"><path d="M5 3l4 0 2 5-2.5 1.8a12 12 0 0 0 5.7 5.7L16 13l5 2v4a2 2 0 0 1-2 2C10 21 2 13 2 5a2 2 0 0 1 3-2z"/></svg>
        <span>+972-70-7654321</span>
      </li>
      <li class="contact">
        <svg viewBox="0 0 22 24" aria-hidden="true"><path d="M1 6h20v2l-10 6L1 8zm0 4.5l10 6 10-6V19H1z"/></svg>
        <span>noam@velmoria-studio.example</span>
      </li>
    </ul>

    <svg class="footer-shape" width="1105" height="631" viewBox="0 0 1105 631" aria-hidden="true">
      <rect x="0" y="615" width="640" height="16" fill="var(--teal)"/>
      <path d="M568 631 L622 586 Q636 574 656 574 L1105 574 L1105 631 Z" fill="var(--card)"/>
      <path d="M578 631 L628 590 Q641 579 660 579 L1105 579 L1105 631 Z" fill="var(--teal)"/>
    </svg>
    <div class="website">www.velmoria-studio.example</div>
  </div>
</body>
</html>
```